Corporate holiday party invitation

Please design a holiday party invitations that looks classy and festive for our member holiday party. The event is first class, semi-formal and needs to be conveyed as such. Please see file from last year so you can see what we are aiming for. The new wording for the invite is as follows: (please use similar fonts to the file provided)

Corvane Members Circle
cordially invites you and a guest to the
Yearly Winter Guild Supper Soiree
on Thursday, December 16th
at 6:30pm in the evening

Merrow Tower, Lantern Club
4817 Pell Avenue, 40th floor
Dallas, TX 75288

Tickets are $100 per person and include:
open premium bar, appetizers, three course dinner
and entertainment

Holiday Cocktail Dress

Target Market(s)

middle aged corporate types

Industry/Entity Type

Event

Font styles to use
Script

Requirements
Must have
• Classy holiday feel and design elements,

```html
<!DOCTYPE html>
<html lang="en">
<head>
<meta charset="UTF-8">
<title>Corvane Members Circle — Yearly Winter Guild Supper Soiree</title>
<link href="https://fonts.googleapis.com/css2?family=Cinzel:wght@400;600&family=Cormorant+Garamond:wght@500;600;700&display=swap" rel="stylesheet">
<style>
  :root {
    --paper: #f4ecd8;
    --paper-edge: #e2d3b2;
    --ink-brown: #4b2f15;
    --gold: #a5722e;
    --gold-soft: #c79a5a;
    --ribbon: #6e4520;
    --ribbon-dark: #4e3015;
    --ribbon-text: #f6ecd6;
    --backdrop: #3a2517;
  }
  * { margin: 0; padding: 0; box-sizing: border-box; }
  html, body { width: 900px; height: 1200px; overflow: hidden; background: var(--backdrop); }
  .invitation {
    position: relative;
    width: 900px;
    height: 1200px;
    background: radial-gradient(ellipse at 50% 45%, var(--paper) 55%, var(--paper-edge) 100%);
    font-family: "Cormorant Garamond", Georgia, serif;
    color: var(--ink-brown);
    text-align: center;
    overflow: hidden;
  }
  .flourish {
    position: absolute;
    width: 270px;
    height: 260px;
  }
  .flourish--top-right {
    top: 18px; right: 18px;
    background: radial-gradient(ellipse at 85% 15%, rgba(165,114,46,0.55) 0%, rgba(199,154,90,0.25) 45%, rgba(199,154,90,0) 72%);
  }
  .flourish--bottom-left {
    bottom: 18px; left: 18px;
    background: radial-gradient(ellipse at 15% 85%, rgba(165,114,46,0.55) 0%, rgba(199,154,90,0.25) 45%, rgba(199,154,90,0) 72%);
  }
  .host {
    position: absolute; top: 200px; left: 0; right: 0;
    font-size: 46px; font-weight: 700; letter-spacing: 0.5px; line-height: 1.1;
  }
  .invite-line {
    position: absolute; top: 262px; left: 0; right: 0;
    font-size: 25px; font-weight: 600; line-height: 1.2;
  }
  .event-name {
    position: absolute; top: 300px; left: 0; right: 0;
    font-family: "Cinzel", "Times New Roman", serif;
    font-size: 28px; font-weight: 400; color: var(--gold); letter-spacing: 1px; line-height: 1.2;
  }
  .date-ribbon {
    position: absolute; top: 352px; left: 50%;
    width: 380px; height: 92px; margin-left: -190px;
  }
  .date-ribbon svg { position: absolute; inset: 0; }
  .date-ribbon p {
    position: relative; padding-top: 16px;
    font-size: 23px; font-weight: 600; line-height: 1.2; color: var(--ribbon-text);
  }
  .venue {
    position: absolute; top: 490px; left: 0; right: 0;
    font-style: normal;
    font-size: 26px; font-weight: 600; line-height: 1.3; color: var(--gold);
  }
  .tickets-heading {
    position: absolute; top: 640px; left: 0; right: 0;
    font-size: 27px; font-weight: 700; letter-spacing: 1.5px; text-transform: uppercase; line-height: 1.2;
  }
  .inclusions {
    position: absolute; top: 700px; left: 0; right: 0;
    list-style: none;
    font-size: 26px; font-weight: 600; line-height: 1.25; color: var(--gold);
  }
  .divider {
    position: absolute; left: 50%; width: 420px; margin-left: -210px;
    height: 2px; background: var(--gold-soft);
  }
  .divider--top { top: 862px; }
  .divider--bottom { top: 945px; }
  .divider-accent {
    position: absolute; top: 851px; left: 50%;
    width: 64px; height: 24px; margin-left: -32px;
    background: radial-gradient(ellipse, var(--gold) 0%, rgba(165,114,46,0.4) 55%, rgba(165,114,46,0) 75%);
  }
  .dress-code {
    position: absolute; top: 890px; left: 0; right: 0;
    font-size: 26px; font-weight: 700; letter-spacing: 1.5px; color: var(--gold); text-transform: uppercase; line-height: 1.2;
  }
</style>
</head>
<body>
<main class="invitation">
  <div class="flourish flourish--top-right" role="img" aria-label="Gold scrollwork corner flourish"></div>
  <div class="flourish flourish--bottom-left" role="img" aria-label="Gold scrollwork corner flourish"></div>

  <h1 class="host">Corvane Members Circle</h1>
  <p class="invite-line">cordially invites you and a guest to the</p>
  <h2 class="event-name">Yearly Winter Guild Supper Soiree</h2>

  <div class="date-ribbon">
    <svg width="380" height="92" viewBox="0 0 380 92" aria-hidden="true">
      <polygon points="0,14 40,14 40,84 0,84 16,49" fill="var(--ribbon-dark)"/>
      <polygon points="380,14 340,14 340,84 380,84 364,49" fill="var(--ribbon-dark)"/>
      <rect x="24" y="4" width="332" height="76" fill="var(--ribbon)"/>
    </svg>
    <p>on Thursday, December 16th<br>at 6:30pm in the evening</p>
  </div>

  <address class="venue">
    Merrow Tower, Lantern Club<br>
    4817 Pell Avenue, 40th floor<br>
    Dallas, TX 75288
  </address>

  <h3 class="tickets-heading">Tickets are $100 per person and include:</h3>
  <ul class="inclusions">
    <li>Open premium bar,</li>
    <li>Appetizers,</li>
    <li>Three course dinner</li>
    <li>And Entertainment</li>
  </ul>

  <div class="divider divider--top"></div>
  <div class="divider-accent" role="img" aria-label="Small gold ornamental divider"></div>
  <p class="dress-code">Holiday Cocktail Dress</p>
  <div class="divider divider--bottom"></div>
</main>
</body>
</html>
```